Breakfast Briefings / Lunch & Learn

I would like to have a double sided flyer size 8x10 to display the breakfast briefing on one side and Lunch & Learn on the other side.

Header on each side to say
2018 Calendar Breakfast Briefing (on the breakfast side)
2018 Calendar Lunch & Learn (on the lunch side)

I have attached a copy of the files we would like to use.

Learn

```html
<!DOCTYPE html>
<html lang="en">
<head>
<meta charset="utf-8">
<title>2018 Calendar – Breakfast Briefings / Lunch &amp; Learn</title>
<link rel="stylesheet" href="https://fonts.googleapis.com/css2?family=Arimo:wght@400;700&display=swap">
<style>
  :root{
    --stage:#2f3133;
    --paper:#ffffff;
    --panel:#f1f1f1;
    --brand-blue:#1a73b0;
    --brand-blue-dark:#15609a;
    --sky:#5e9ec4;
    --sky-light:#a9c8e2;
    --slate:#6d737a;
    --ink:#222a33;
    --logo-ink:#3b4450;
    --icon-teal:#1b8f9a;
  }
  *{margin:0;padding:0;box-sizing:border-box}
  html,body{width:1200px;height:776px;overflow:hidden;background:var(--stage);font-family:"Arimo",Arial,sans-serif}
  .spread{position:relative;width:1200px;height:776px}
  .flyer{position:absolute;top:38px;width:555px;height:700px;background:var(--paper);overflow:hidden}
  .flyer--breakfast{left:30px}
  .flyer--lunch{left:615px}
  .flyer svg{position:absolute;left:0;top:0}
  .header-title{fill:#fff}
  .ring-label{font-size:7px;fill:var(--ink);text-anchor:middle}
  .ring-label .month{font-weight:700}
  .wordmark{font-size:28px;font-weight:400;letter-spacing:3px}
  .agenda-month{font-size:14px;fill:var(--ink)}
  .agenda-topic{font-size:14px;fill:var(--ink)}
</style>
</head>
<body>
<main class="spread">

  <!-- Breakfast Briefings side -->
  <section class="flyer flyer--breakfast" aria-label="2018 Calendar Breakfast Briefings">
    <svg width="555" height="700" viewBox="0 0 555 700">
      <defs>
        <linearGradient id="breakfastPhoto" x1="0" y1="0" x2="1" y2="1">
          <stop offset="0" stop-color="#3f86b6"/>
          <stop offset="1" stop-color="#6ea7c8"/>
        </linearGradient>
        <radialGradient id="tabletPhoto" cx="0.5" cy="0.5" r="0.5">
          <stop offset="0" stop-color="#c9a27a"/>
          <stop offset="1" stop-color="#8a6440"/>
        </radialGradient>
      </defs>

      <!-- header swoosh -->
      <path class="header-swoosh-light" d="M0,150 C300,232 520,190 555,55 V70 C520,215 300,250 0,165 Z" fill="var(--sky-light)"/>
      <path class="header-swoosh-dark" d="M0,140 C300,222 520,180 555,40 V58 C520,200 300,238 0,152 Z" fill="var(--brand-blue)"/>
      <path class="header-photo" role="img" aria-label="Breakfast table with coffee, berries and fruit, tinted blue" d="M0,0 H555 V40 C520,180 300,222 0,140 Z" fill="url(#breakfastPhoto)"/>

      <!-- header title -->
      <line x1="0" y1="78" x2="385" y2="72" stroke="#fff" stroke-width="1.5"/>
      <g class="cup-icon" fill="none" stroke="#fff" stroke-width="2">
        <path d="M70,80 h26 v6 a13,11 0 0 1 -26,0 z"/>
        <path d="M96,82 a5,5 0 0 1 0,9"/>
        <path d="M64,99 h38"/>
        <path d="M83,74 c-4,-5 4,-8 0,-14"/>
      </g>
      <text class="header-title" x="108" y="64" font-size="15">2018 Calendar</text>
      <text class="header-title" x="120" y="90" font-size="21">Breakfast</text>
      <text class="header-title" x="185" y="114" font-size="21">Briefings</text>

      <!-- department cycle -->
      <circle cx="255" cy="400" r="118" fill="url(#tabletPhoto)" role="img" aria-label="Tablet on a wooden desk showing the 2018 Calendar Breakfast Briefings title"/>

      <g class="cycle-arrows">
        <path d="M-5,-5 L5,0 L-5,5 Z" fill="#f2d000" transform="translate(255,240.6) rotate(0)"/>
        <path d="M-5,-5 L5,0 L-5,5 Z" fill="#d8e612" transform="translate(334.7,262) rotate(30)"/>
        <path d="M-5,-5 L5,0 L-5,5 Z" fill="#a6e01e" transform="translate(393,320.3) rotate(60)"/>
        <path d="M-5,-5 L5,0 L-5,5 Z" fill="#7fd824" transform="translate(414.4,400) rotate(90)"/>
        <path d="M-5,-5 L5,0 L-5,5 Z" fill="#4fd22b" transform="translate(393,479.7) rotate(120)"/>
        <path d="M-5,-5 L5,0 L-5,5 Z" fill="#2fd03d" transform="translate(334.7,538) rotate(150)"/>
        <path d="M-5,-5 L5,0 L-5,5 Z" fill="#2bd06a" transform="translate(255,559.4) rotate(180)"/>
        <path d="M-5,-5 L5,0 L-5,5 Z" fill="#2dd095" transform="translate(175.3,538) rotate(210)"/>
        <path d="M-5,-5 L5,0 L-5,5 Z" fill="#30c6b6" transform="translate(117,479.7) rotate(240)"/>
        <path d="M-5,-5 L5,0 L-5,5 Z" fill="#36b6cc" transform="translate(95.6,400) rotate(270)"/>
        <path d="M-5,-5 L5,0 L-5,5 Z" fill="#3a94d0" transform="translate(117,320.3) rotate(300)"/>
        <path d="M-5,-5 L5,0 L-5,5 Z" fill="#f0a400" transform="translate(175.3,262) rotate(330)"/>
      </g>

      <g class="cycle-nodes">
        <circle cx="212.3" cy="240.6" r="32" fill="#f5a800"/>
        <text class="ring-label" x="212.3" y="232"><tspan x="212.3">Medical</tspan><tspan x="212.3" dy="8">Owen Marsh</tspan><tspan x="212.3" dy="8" class="month">2019</tspan><tspan x="212.3" dy="8" class="month">TBD</tspan></text>

        <circle cx="297.7" cy="240.6" r="32" fill="#f2e600"/>
        <text class="ring-label" x="297.7" y="232"><tspan x="297.7">Sales</tspan><tspan x="297.7" dy="8">Leo Brandt</tspan><tspan x="297.7" dy="8" class="month">2019</tspan><tspan x="297.7" dy="8" class="month">TBD</tspan></text>

        <circle cx="371.7" cy="283.3" r="32" fill="#c8e61e"/>
        <text class="ring-label" x="371.7" y="278"><tspan x="371.7">Finance</tspan><tspan x="371.7" dy="8">Sam Porter</tspan><tspan x="371.7" dy="10" class="month">March</tspan></text>

        <circle cx="414.4" cy="357.3" r="32" fill="#8fdc1e"/>
        <text class="ring-label" x="414.4" y="348"><tspan x="414.4">R&amp;D</tspan><tspan x="414.4" dy="8">Nina</tspan><tspan x="414.4" dy="8">Castellano</tspan><tspan x="414.4" dy="10" class="month">April</tspan></text>

        <circle cx="414.4" cy="442.7" r="32" fill="#5fd42a"/>
        <text class="ring-label" x="414.4" y="434"><tspan x="414.4">Operations</tspan><tspan x="414.4" dy="8">Adam</tspan><tspan x="414.4" dy="8">Kessler</tspan><tspan x="414.4" dy="10" class="month">May</tspan></text>

        <circle cx="371.7" cy="516.7" r="32" fill="#2fd02f"/>
        <text class="ring-label" x="371.7" y="511"><tspan x="371.7">Clinical / Reg</tspan><tspan x="371.7" dy="8">Tom Heller</tspan><tspan x="371.7" dy="10" class="month">June</tspan></text>

        <circle cx="297.7" cy="559.4" r="32" fill="#2bd05a"/>
        <text class="ring-label" x="297.7" y="551"><tspan x="297.7">Quality</tspan><tspan x="297.7" dy="8">Mark</tspan><tspan x="297.7" dy="8">Ellington</tspan><tspan x="297.7" dy="10" class="month">July</tspan></text>

        <circle cx="212.3" cy="559.4" r="32" fill="#2dd48a"/>
        <text class="ring-label" x="212.3" y="554"><tspan x="212.3">People</tspan><tspan x="212.3" dy="8">Rita Sharma</tspan><tspan x="212.3" dy="10" class="month">August</tspan></text>

        <circle cx="138.3" cy="516.7" r="32" fill="#2ec9b0"/>
        <text class="ring-label" x="138.3" y="511"><tspan x="138.3">Marketing</tspan><tspan x="138.3" dy="8">Vikram Desai</tspan><tspan x="138.3" dy="10" class="month">September</tspan></text>

        <circle cx="95.6" cy="442.7" r="32" fill="#33bcc8"/>
        <text class="ring-label" x="95.6" y="437"><tspan x="95.6">Legal</tspan><tspan x="95.6" dy="8">Omar Haddad</tspan><tspan x="95.6" dy="10" class="month">October</tspan></text>

        <circle cx="95.6" cy="357.3" r="32" fill="#3a9fd0"/>
        <text class="ring-label" x="95.6" y="348"><tspan x="95.6">Market Access</tspan><tspan x="95.6" dy="8">Laura</tspan><tspan x="95.6" dy="8">Whitfield</tspan><tspan x="95.6" dy="10" class="month">November</tspan></text>

        <circle cx="138.3" cy="283.3" r="32" fill="#3a78c8"/>
        <text class="ring-label" x="138.3" y="278" fill="#fff"><tspan x="138.3" fill="#fff">FCS</tspan><tspan x="138.3" dy="8" fill="#fff">Dana Whitlock</tspan><tspan x="138.3" dy="10" class="month" fill="#fff">December</tspan></text>
      </g>

      <!-- brand -->
      <rect x="30" y="622" width="14" height="14" fill="var(--brand-blue)"/>
      <text class="wordmark" x="52" y="638" fill="var(--logo-ink)">veltra</text>

      <!-- bottom band -->
      <path d="M0,668 H250 L268,690 V700 H0 Z" fill="var(--brand-blue)"/>
      <path d="M250,668 H555 V700 H268 L268,690 Z" fill="var(--slate)"/>
      <path d="M238,668 H250 L268,690 V700 H258 L258,690 Z" fill="var(--paper)"/>
    </svg>
  </section>

  <!-- Lunch & Learn side -->
  <section class="flyer flyer--lunch" aria-label="2018 Calendar Lunch and Learn">
    <svg width="555" height="700" viewBox="0 0 555 700">
      <defs>
        <linearGradient id="lunchPhoto" x1="0" y1="0" x2="1" y2="1">
          <stop offset="0" stop-color="#4a8fba"/>
          <stop offset="1" stop-color="#7db2cf"/>
        </linearGradient>
      </defs>

      <!-- header -->
      <rect class="header-photo" role="img" aria-label="Lunch table with salads and plates, tinted blue" x="0" y="0" width="555" height="140" fill="url(#lunchPhoto)"/>
      <rect x="0" y="140" width="555" height="6" fill="var(--sky-light)"/>

      <g class="cloche-icon" fill="#fff">
        <path d="M30,82 a26,24 0 0 1 52,0 Z"/>
        <rect x="26" y="84" width="60" height="5" rx="2"/>
        <circle cx="56" cy="55" r="4"/>
      </g>
      <line x1="0" y1="94" x2="110" y2="94" stroke="#fff" stroke-width="1.5"/>
      <text class="header-title" x="110" y="60" font-size="15">2018 Calendar</text>
      <text class="header-title" x="118" y="92" font-size="28">Lunch &amp;</text>
      <text class="header-title" x="200" y="122" font-size="28">Learn</text>
      <line x1="270" y1="124" x2="355" y2="124" stroke="#fff" stroke-width="1.5"/>

      <!-- agenda panel -->
      <rect x="0" y="146" width="420" height="504" fill="var(--panel)"/>
      <rect class="side-column" role="img" aria-label="Blue column with faint cutlery and pencil motif" x="430" y="146" width="125" height="494" fill="var(--brand-blue)"/>

      <g class="agenda">
        <g transform="translate(40,175)">
          <rect x="0" y="-12" width="15" height="15" rx="2" fill="none" stroke="var(--icon-teal)" stroke-width="2"/>
          <path d="M4,-8 h7 v5 h-4 l-2,2 v-2 h-1 z" fill="var(--icon-teal)"/>
          <text class="agenda-month" x="26" y="0">March:</text>
          <text class="agenda-topic" x="30" y="17">Mindfulness</text>
        </g>
        <g transform="translate(40,224)">
          <rect x="0" y="-12" width="15" height="15" rx="2" fill="none" stroke="var(--icon-teal)" stroke-width="2"/>
          <path d="M4,-8 h7 v5 h-4 l-2,2 v-2 h-1 z" fill="var(--icon-teal)"/>
          <text class="agenda-month" x="26" y="0">April:</text>
          <text class="agenda-topic" x="30" y="17">Nutrition and Lifestyle Coaching</text>
        </g>
        <g transform="translate(40,273)">
          <rect x="0" y="-12" width="15" height="15" rx="2" fill="none" stroke="var(--icon-teal)" stroke-width="2"/>
          <path d="M4,-8 h7 v5 h-4 l-2,2 v-2 h-1 z" fill="var(--icon-teal)"/>
          <text class="agenda-month" x="26" y="0">May:</text>
          <text class="agenda-topic" x="30" y="17">What is Neuromodulation?</text>
        </g>
        <g transform="translate(40,322)">
          <rect x="0" y="-12" width="15" height="15" rx="2" fill="none" stroke="var(--icon-teal)" stroke-width="2"/>
          <path d="M4,-8 h7 v5 h-4 l-2,2 v-2 h-1 z" fill="var(--icon-teal)"/>
          <text class="agenda-month" x="26" y="0">June:</text>
          <text class="agenda-topic" x="30" y="17">Achieve Your Goals</text>
        </g>
        <g transform="translate(40,371)">
          <rect x="0" y="-12" width="15" height="15" rx="2" fill="none" stroke="var(--icon-teal)" stroke-width="2"/>
          <path d="M4,-8 h7 v5 h-4 l-2,2 v-2 h-1 z" fill="var(--icon-teal)"/>
          <text class="agenda-month" x="26" y="0">July:</text>
          <text class="agenda-topic" x="30" y="17">Changing Your LifePositive Thinking</text>
        </g>
        <g transform="translate(40,420)">
          <rect x="0" y="-12" width="15" height="15" rx="2" fill="none" stroke="var(--icon-teal)" stroke-width="2"/>
          <path d="M4,-8 h7 v5 h-4 l-2,2 v-2 h-1 z" fill="var(--icon-teal)"/>
          <text class="agenda-month" x="26" y="0">August:</text>
          <text class="agenda-topic" x="30" y="17">Clean EatingHow Do I Get Started</text>
        </g>
        <g transform="translate(40,469)">
          <rect x="0" y="-12" width="15" height="15" rx="2" fill="none" stroke="var(--icon-teal)" stroke-width="2"/>
          <path d="M4,-8 h7 v5 h-4 l-2,2 v-2 h-1 z" fill="var(--icon-teal)"/>
          <text class="agenda-month" x="26" y="0">September:</text>
          <text class="agenda-topic" x="30" y="17">Budgeting 101 Financial Wellness</text>
        </g>
        <g transform="translate(40,518)">
          <rect x="0" y="-12" width="15" height="15" rx="2" fill="none" stroke="var(--icon-teal)" stroke-width="2"/>
          <path d="M4,-8 h7 v5 h-4 l-2,2 v-2 h-1 z" fill="var(--icon-teal)"/>
          <text class="agenda-month" x="26" y="0">October:</text>
          <text class="agenda-topic" x="30" y="17">Busted! Nutrition Myths</text>
        </g>
        <g transform="translate(40,567)">
          <rect x="0" y="-12" width="15" height="15" rx="2" fill="none" stroke="var(--icon-teal)" stroke-width="2"/>
          <path d="M4,-8 h7 v5 h-4 l-2,2 v-2 h-1 z" fill="var(--icon-teal)"/>
          <text class="agenda-month" x="26" y="0">November:</text>
          <text class="agenda-topic" x="30" y="17">Time Management</text>
        </g>
        <g transform="translate(40,616)">
          <rect x="0" y="-12" width="15" height="15" rx="2" fill="none" stroke="var(--icon-teal)" stroke-width="2"/>
          <path d="M4,-8 h7 v5 h-4 l-2,2 v-2 h-1 z" fill="var(--icon-teal)"/>
          <text class="agenda-month" x="26" y="0">December:</text>
          <text class="agenda-topic" x="30" y="17">First Time Home Buyers</text>
        </g>
      </g>

      <!-- brand on blue column -->
      <rect x="444" y="548" width="10" height="10" fill="#fff"/>
      <text class="wordmark" x="460" y="560" fill="#fff" font-size="22">veltra</text>

      <!-- bottom band -->
      <path d="M0,656 H555 V700 H0 Z" fill="var(--brand-blue)"/>
      <path d="M420,650 H555 V676 H400 Z" fill="var(--slate)"/>
      <path d="M420,650 H430 L412,676 H400 Z" fill="var(--paper)"/>
    </svg>
  </section>

</main>
</body>
</html>
```